Mezzanine Floor Manufacturer looking for a new business card design

We manufacture mezzanine floors and are providers of racking systems. We provide a range of items/services - simple rack repairs , full warehouse fit outs , manufacturer and install mezzanine floors , partitioning and large turnkey projects. Recently had a new website - www.corvane-shelving.co.uk and would like our business cards updating aswell . Our current card is single sided in the old logo colours (pdf attached) and needs updating.

Target Market(s)

We deal with large projects/ multi national companies and also smaller projects and companies throughout the UK ranging from a single warehouse to a large multi site company.

Industry/Entity Type

Business

Contact Information for Business Card

Will have job title,tel no's, email ,website address etc like example pdf

Requirements
Must have
• Hi - needs to use the colours of the logo & new website. Card needs to be professional

```html
<!DOCTYPE html>
<html lang="en">
<head>
<meta charset="utf-8">
<title>Corvane business card</title>
<link rel="stylesheet" href="https://fonts.googleapis.com/css2?family=Arimo:ital,wght@0,400;0,700;1,400&display=swap">
<style>
  :root {
    --brand-red: #c4161c;
    --brand-red-dark: #a81218;
    --card-white: #ffffff;
    --ink-grey: #555555;
    --soft-white: rgba(255,255,255,0.82);
    --page-bg: #e9e6e1;
  }
  * { box-sizing: border-box; margin: 0; padding: 0; }
  html, body { width: 1200px; height: 950px; overflow: hidden; }
  body {
    background: var(--page-bg);
    font-family: "Arimo", Arial, sans-serif;
    position: relative;
  }
  .card {
    position: absolute;
    left: 280px;
    width: 640px;
    height: 376px;
    box-shadow: 0 10px 28px rgba(0,0,0,0.22);
    overflow: hidden;
  }
  .card-front { top: 70px; background: var(--brand-red); color: var(--card-white); }
  .card-back { top: 500px; background: var(--card-white); }

  /* front */
  .front-brand {
    position: absolute; top: 118px; left: 0; right: 0;
    display: flex; align-items: center; justify-content: center; gap: 14px;
  }
  .brand-dot { width: 30px; height: 30px; border-radius: 50%; background: var(--card-white); }
  .front-brand .brand-name {
    font-weight: 700; font-size: 54px; letter-spacing: 0.5px; color: var(--card-white);
  }
  .front-web {
    position: absolute; top: 214px; left: 0; right: 0; text-align: center;
    font-style: italic; font-size: 17px; letter-spacing: 4px; color: var(--soft-white);
  }
  .social-row {
    position: absolute; top: 130px; right: 22px; display: flex; gap: 6px;
  }
  .social-row span { width: 16px; height: 16px; border-radius: 50%; background: var(--card-white); }

  /* back */
  .back-brand {
    position: absolute; top: 34px; left: 44px;
    display: flex; align-items: center; gap: 12px;
  }
  .back-brand .brand-dot { background: var(--brand-red); width: 34px; height: 34px; }
  .back-brand .brand-name { font-weight: 700; font-size: 46px; color: var(--brand-red); }
  .address {
    position: absolute; top: 108px; left: 48px;
    font-size: 15px; line-height: 19px; color: var(--ink-grey);
  }
  .contact-list {
    position: absolute; top: 168px; left: 30px; list-style: none;
    font-size: 15px; line-height: 20px; color: var(--ink-grey);
  }
  .contact-list li { display: flex; align-items: center; gap: 7px; }
  .contact-list svg { width: 12px; height: 12px; fill: var(--brand-red); flex: none; }
  .person {
    position: absolute; right: 70px; bottom: 62px; text-align: right;
  }
  .person-name { font-size: 22px; color: var(--brand-red); }
  .person-role { font-size: 17px; color: var(--ink-grey); margin-top: 2px; }
  .edge-bar {
    position: absolute; right: 0; bottom: 40px; width: 30px; height: 36px;
    background: var(--brand-red);
  }
</style>
</head>
<body>

<section class="card card-front" aria-label="Card front">
  <div class="front-brand">
    <span class="brand-dot"></span>
    <span class="brand-name">Corvane</span>
  </div>
  <p class="front-web">www.corvane-shelving.co.uk</p>
  <div class="social-row" aria-label="Social links">
    <span></span><span></span><span></span><span></span>
  </div>
</section>

<section class="card card-back" aria-label="Card back">
  <div class="back-brand">
    <span class="brand-dot"></span>
    <span class="brand-name">Corvane</span>
  </div>
  <address class="address" style="font-style:normal">
    Tallow brook close<br>
    fenwick gate business Park<br>
    alford, Derbyshire De7 4rK
  </address>
  <ul class="contact-list">
    <li><svg viewBox="0 0 12 12"><path d="M2.5 1l2 2-1 1.5c.7 1.5 1.8 2.6 3.3 3.3L8.3 6.8l2 2-1.3 1.9C5 10.5 1.5 7 1.3 2.3z"/></svg>01632 960481</li>
    <li><svg viewBox="0 0 12 12"><rect x="3" y="0.5" width="6" height="11" rx="1"/><rect x="4" y="2" width="4" height="6.5" fill="#fff"/></svg>07700 900352</li>
    <li><svg viewBox="0 0 12 12"><path d="M2.5 1l2 2-1 1.5c.7 1.5 1.8 2.6 3.3 3.3L8.3 6.8l2 2-1.3 1.9C5 10.5 1.5 7 1.3 2.3z"/></svg>01632 960977</li>
    <li><svg viewBox="0 0 12 12"><rect x="0.5" y="2" width="11" height="8"/><path d="M1 2.5l5 4 5-4" stroke="#fff" stroke-width="1.2" fill="none"/></svg>ellis@corvane-shelving.co.uk</li>
    <li><svg viewBox="0 0 12 12"><circle cx="6" cy="6" r="5.5"/><path d="M.5 6h11M6 .5c-2.5 3-2.5 8 0 11M6 .5c2.5 3 2.5 8 0 11" stroke="#fff" stroke-width="0.9" fill="none"/></svg>www.corvane-shelving.co.uk</li>
  </ul>
  <div class="person">
    <p class="person-name">Ellis Marwood</p>
    <p class="person-role">Technical sales</p>
  </div>
  <span class="edge-bar"></span>
</section>

</body>
</html>
```